Website Design for WeselneKarety.pl – Luxury Wedding Car Rental with Chauffeur

We are looking for a talented designer to create a modern, elegant, and fully responsive website for our new brand – WeselnyKarety.pl. We are a premium car rental platform in Poland, offering luxury and exotic vehicles exclusively for weddings. All cars come with a professional chauffeur, ensuring a high-end, stress-free, and stylish experience.
Website Purpose:
The website should present our offering in a luxurious, clear, and inspiring way. It must build trust, highlight the prestige of our brand, and encourage inquiries. Our target audience includes engaged couples, wedding planners, and clients seeking a truly exceptional vehicle for their special day.
Design Requirements:
Style: modern, elegant, minimalist
Color palette: white, black, gold, optionally silver – refined and luxurious
Typography: clean, modern, high-end
Layout: clear, intuitive, with large car images and well-defined sections
Fully responsive (desktop, tablet, mobile)
Bilingual layout (Polish/English) must be considered
Pages to Design:
Homepage
About Us
Fleet Overview
Individual Car Pages
Services (Weddings, Photo Shoots, Film Rentals)
Why Us / Unique Selling Points
Contact
FAQ
Inspiration:
Luxury automotive brands (e.g. Varnell-Dorne, Corwick, Elsby Havard)
High-end wedding websites
Minimalist layouts with large visuals and elegant typography
Additional Notes:
The design should evoke the emotions of a wedding day – elegance, uniqueness, style, and class. Please avoid flashy colors, excessive graphic effects, or overly decorative elements. Subtlety, prestige, and sophistication are key.

```html
<!DOCTYPE html>
<html lang="en">
<head>
<meta charset="utf-8">
<title>WeselneKarety.pl – Luxury Wedding Cars with Chauffeur</title>
<link href="https://fonts.googleapis.com/css2?family=Playfair+Display:wght@500;600&family=Poppins:wght@400;500&family=Great+Vibes&display=swap" rel="stylesheet">
<style>
:root{
  --gold:#d8bf60;
  --gold-text:#cdb15a;
  --ink:#111111;
  --muted:#222;
  --paper:#ffffff;
  --sand:#f0efeb;
  --line:#444;
  --footer:#000000;
  --heading:"Playfair Display", Georgia, serif;
  --body:"Poppins", Arial, sans-serif;
  --script:"Great Vibes", cursive;
}
*{margin:0;padding:0;box-sizing:border-box}
html,body{width:1200px;height:3665px;overflow:hidden}
body{position:relative;background:var(--paper);color:var(--ink);font-family:var(--body)}
.abs{position:absolute}
.heading{font-family:var(--heading);font-weight:500;text-transform:uppercase;color:var(--ink);text-align:center;letter-spacing:-.3px}
.script{font-family:var(--script);color:var(--gold-text);text-align:center}
.btn{position:absolute;display:flex;align-items:center;justify-content:center;background:var(--gold);border-radius:30px;font-family:var(--heading);font-size:10px;font-weight:600;text-transform:uppercase;color:var(--ink);box-shadow:0 0 0 3px #fff,0 0 0 4px var(--gold)}
.photo{position:absolute}

/* nav */
.site-nav{left:0;top:0;width:1200px;height:58px;background:#fff}
.brand{display:flex;align-items:center;gap:8px;font-family:var(--heading);font-size:19px;color:var(--gold-text)}
.brand-dot{width:10px;height:10px;border-radius:50%;background:var(--gold)}
.nav-links{left:487px;top:20px;display:flex;gap:32px;font-family:var(--heading);font-size:10.5px;font-weight:500;text-transform:uppercase}
.nav-links .active{border-bottom:2px solid var(--gold);padding-bottom:19px}

/* hero */
.hero{left:0;top:58px;width:1200px;height:723px;background:linear-gradient(160deg,#6f6a1e 0%,#a58a2e 30%,#3c4a2a 55%,#d9d6cf 75%,#5a4a1c 100%)}
.hero-panel{left:210px;top:309px;width:782px;height:247px;background:rgba(110,110,110,.72)}
.hero-title{left:210px;top:372px;width:782px;font-size:43px;line-height:53px;color:#fff}
.hero-sub{left:210px;top:483px;width:782px;text-align:center;color:#fff;font-size:12px}

/* about */
.about-block{left:0;top:931px;width:182px;height:278px;background:var(--sand)}
.about-title{left:380px;top:1040px;width:420px;font-size:29px;line-height:38px}
.about-text{left:408px;top:1122px;width:355px;text-align:center;font-size:10.5px;line-height:16.5px}

/* features */
.feature{top:1415px;width:200px;text-align:center;font-family:var(--heading);font-size:11px;font-weight:500;text-transform:uppercase;line-height:17px}
.feature svg{display:block;margin:0 auto 6px}
.divider-v{width:1px;background:var(--gold)}

/* fleet */
.fleet{left:0;top:1570px;width:1200px;height:634px;background:var(--sand)}
.car-card{top:1757px;width:266px;height:367px;border:1px solid #333;background:transparent}
.car-card .photo{left:5px;top:5px;width:254px;height:241px}
.car-badge{left:103px;top:218px;width:60px;height:30px}
.car-name{top:272px;width:100%;text-align:center;font-family:var(--heading);font-size:11px;font-weight:600;text-transform:uppercase}
.car-desc{top:291px;left:25px;width:216px;text-align:center;font-size:10.5px;line-height:16px}
.car-link{top:334px;width:100%;text-align:center;font-family:var(--heading);font-size:10px;color:var(--gold-text);text-transform:uppercase}

/* services */
.service-card{left:607px;top:2323px;width:349px;height:340px;background:#fff;box-shadow:0 4px 22px rgba(0,0,0,.12)}

/* testimonials */
.review{background:#fff;border:1px solid #e7e7e7;padding:20px 20px}
.stars{color:#e8a317;font-size:17px;letter-spacing:3px}
.quote{font-size:11.5px;line-height:16.5px;margin-top:6px}
.client{display:flex;align-items:center;gap:14px;margin-top:8px;font-family:var(--heading);font-size:12px;font-weight:600;text-transform:uppercase}
.avatar{width:30px;height:30px;border-radius:50%;background:#e9c9c9}
.dots{left:574px;top:3010px;display:flex;gap:7px}
.dots span{width:7px;height:7px;border-radius:50%;background:#c8c8c8}
.dots .on{background:var(--gold)}

/* cta */
.cta{left:0;top:3082px;width:1200px;height:235px;background:var(--gold)}

/* footer */
.footer{left:0;top:3317px;width:1200px;height:348px;background:var(--footer);color:#fff}
.footer-links{left:0;top:3446px;width:1200px;display:flex;justify-content:center;gap:48px;font-size:11.5px;color:#fff}
.hline{height:1px;background:#bbb}
.contact-col{top:3515px;text-align:center;color:#fff}
.contact-col h3{font-family:var(--heading);font-weight:500;font-size:20px;text-transform:uppercase}
.contact-col p{font-size:11.5px;line-height:14px;margin-top:4px}
.socials{left:536px;top:3588px;display:flex;gap:10px}
.socials span{width:24px;height:24px;border-radius:50%;border:1px solid #fff;background:#000}
.copy{left:0;top:3630px;width:1200px;text-align:center;font-size:11.5px;color:#fff}
</style>
</head>
<body>

<!-- navigation -->
<header class="abs site-nav">
  <div class="abs brand" style="left:75px;top:17px"><span class="brand-dot"></span>WeselneKarety</div>
  <nav class="abs nav-links">
    <span class="active">Home</span><span>About Us</span><span>Fleet</span><span>Services</span><span>Why Us</span><span>FAQ</span><span>Contact</span>
  </nav>
  <div class="btn" style="left:993px;top:10px;width:130px;height:38px">Book Now</div>
</header>

<!-- hero -->
<section class="abs hero" role="img" aria-label="Bride in a white gown beside a vintage yellow and green car on an autumn forest road"></section>
<div class="abs hero-panel"></div>
<h1 class="abs heading hero-title">Arrive in Elegance,<br>Leave a Lasting Impression</h1>
<p class="abs hero-sub">Luxury &amp; Exotic Cars with Chauffeur for Your Perfect Wedding Day</p>

<!-- about -->
<div class="abs about-block"></div>
<div class="photo" style="left:123px;top:997px;width:203px;height:292px;background:linear-gradient(180deg,#ece4e4 0%,#cfc6b8 40%,#a9a79a 70%,#6f7a4c 100%)" role="img" aria-label="White vintage convertible decorated with a green floral garland"></div>
<div class="photo" style="left:826px;top:849px;width:303px;height:507px;background:linear-gradient(170deg,#c9a57c 0%,#b8926a 35%,#d24d9a 65%,#9a7a5c 100%)" role="img" aria-label="Wedding couple sitting on a pink classic car decorated with flowers"></div>
<div class="photo" style="left:552px;top:908px;width:80px;height:92px;background:radial-gradient(ellipse at center,#e8d7c6 0%,#fff 70%)" role="img" aria-label="Delicate botanical sprig ornament"></div>
<p class="abs script" style="left:380px;top:1003px;width:420px;font-size:24px">About Weselne Karety</p>
<h2 class="abs heading about-title">Driven by Elegance,<br>Inspired by Love</h2>
<p class="abs about-text">WeselnyKarety.pl was born from a passion for luxury cars and the desire to make every wedding truly unforgettable. Our team is dedicated to providing a first-class experience, ensuring that every moment feels exceptional.</p>
<div class="btn" style="left:520px;top:1217px;width:130px;height:40px">Read More</div>

<!-- features -->
<div class="abs feature" style="left:151px">
  <svg width="76" height="48" viewBox="0 0 76 48" fill="none" stroke="#111" stroke-width="2"><path d="M8 24 L16 8 H60 L68 24"/><rect x="4" y="24" width="68" height="16" rx="4"/><rect x="10" y="40" width="10" height="6"/><rect x="56" y="40" width="10" height="6"/><circle cx="15" cy="31" r="3"/><circle cx="61" cy="31" r="3"/><path d="M26 32 H50"/></svg>
  Luxury Cars,<br>Spotless and Elegant
</div>
<div class="abs divider-v" style="left:353px;top:1417px;height:92px"></div>
<div class="abs feature" style="left:379px">
  <svg width="48" height="48" viewBox="0 0 48 48" fill="none" stroke="#111" stroke-width="2"><path d="M14 12 H34 L32 6 H16 Z"/><circle cx="24" cy="18" r="7"/><path d="M8 46 V38 Q8 28 24 28 Q40 28 40 38 V46"/><circle cx="24" cy="39" r="6"/></svg>
  Professional,<br>Experienced Chauffeurs
</div>
<div class="abs divider-v" style="left:606px;top:1417px;height:92px"></div>
<div class="abs feature" style="left:624px">
  <svg width="70" height="48" viewBox="0 0 70 48" fill="none" stroke="#111" stroke-width="2"><circle cx="22" cy="12" r="7"/><circle cx="48" cy="12" r="7"/><path d="M8 46 V32 Q8 22 22 22 Q34 22 34 32 V46"/><path d="M36 46 L38 30 Q40 22 48 22 Q56 22 58 30 L62 46"/></svg>
  Personalized<br>Service for Every Couple
</div>
<div class="abs divider-v" style="left:847px;top:1417px;height:92px"></div>
<div class="abs feature" style="left:853px">
  <svg width="56" height="48" viewBox="0 0 56 48" fill="none" stroke="#111" stroke-width="2"><circle cx="14" cy="12" r="9"/><path d="M14 7 V12 H18"/><path d="M12 34 L18 24 H40 L48 34"/><rect x="8" y="34" width="44" height="8" rx="3"/><circle cx="18" cy="44" r="3"/><circle cx="42" cy="44" r="3"/></svg>
  On-Time, Stress Free,<br>Stylish Rides
</div>

<!-- fleet -->
<section class="abs fleet"></section>
<p class="abs script" style="left:0;top:1632px;width:1200px;font-size:24px">Our Fleet</p>
<h2 class="abs heading" style="left:0;top:1669px;width:1200px;font-size:30px">Choose Your Dream Car</h2>
<p class="abs" style="left:0;top:1712px;width:1200px;text-align:center;font-size:11px">From Varnell-Dorne to Castora explore our carefully curated collection of high-end vehicles.</p>

<div class="abs car-card" style="left:187px">
  <div class="photo" style="background:linear-gradient(180deg,#9fb8cc 0%,#6f8a58 40%,#1d2a25 70%,#b9b2a5 100%)" role="img" aria-label="Dark green luxury saloon parked among palm trees"></div>
  <svg class="abs car-badge" viewBox="0 0 60 30"><path d="M0 30 L30 0 L60 30 Z" fill="#fff"/><g fill="none" stroke="#111" stroke-width="1.5"><rect x="20" y="12" width="20" height="14" rx="2"/><path d="M24 15 V23 M28 15 V23 M32 15 V23 M36 15 V23"/></g></svg>
  <div class="abs car-name">Varnell-Dorne</div>
  <div class="abs car-desc">From Varnell-Dorne to Castora explore our carefully curated collection.</div>
  <div class="abs car-link">View Details</div>
</div>
<div class="abs car-card" style="left:467px">
  <div class="photo" style="background:linear-gradient(180deg,#dcdcd6 0%,#b8b7ae 40%,#3c5a6e 65%,#8d8a80 100%)" role="img" aria-label="Blue grand touring saloon parked by the sea"></div>
  <svg class="abs car-badge" viewBox="0 0 60 30"><path d="M0 30 L30 0 L60 30 Z" fill="#fff"/><g fill="none" stroke="#111" stroke-width="1.5"><path d="M18 20 L22 12 H38 L42 20"/><rect x="16" y="20" width="28" height="7" rx="2"/></g></svg>
  <div class="abs car-name">Corwick</div>
  <div class="abs car-desc">From Varnell-Dorne to Castora explore our carefully curated collection.</div>
  <div class="abs car-link">View Details</div>
</div>
<div class="abs car-card" style="left:748px">
  <div class="photo" style="background:linear-gradient(180deg,#9aa7a8 0%,#6a7a52 40%,#8c9094 65%,#a8a49a 100%)" role="img" aria-label="Silver sports coupé parked in front of green hills"></div>
  <svg class="abs car-badge" viewBox="0 0 60 30"><path d="M0 30 L30 0 L60 30 Z" fill="#fff"/><g fill="none" stroke="#111" stroke-width="1.5"><path d="M18 20 L22 12 H38 L42 20"/><rect x="16" y="20" width="28" height="7" rx="2"/></g></svg>
  <div class="abs car-name">Elsby Havard</div>
  <div class="abs car-desc">From Varnell-Dorne to Castora explore our carefully curated collection</div>
  <div class="abs car-link">View Details</div>
</div>

<!-- services -->
<div class="photo" style="left:243px;top:2270px;width:411px;height:367px;background:linear-gradient(160deg,#e6e6e6 0%,#9a9488 40%,#c6a97a 60%,#3d3a36 100%)" role="img" aria-label="Newlyweds walking away under falling petals while guests celebrate"></div>
<div class="abs service-card"></div>
<p class="abs script" style="left:636px;top:2368px;font-size:23px;text-align:left">Our Services</p>
<h2 class="abs heading" style="left:636px;top:2398px;font-size:29px;line-height:37px;text-align:left">More Than Just<br>a Ride</h2>
<svg class="abs" style="left:638px;top:2490px" width="52" height="52" viewBox="0 0 52 52" fill="none" stroke="#111" stroke-width="2"><rect x="2" y="14" width="48" height="34" rx="4"/><path d="M16 14 L20 6 H32 L36 14"/><circle cx="26" cy="31" r="10"/><circle cx="26" cy="31" r="5"/><rect x="6" y="18" width="7" height="4"/></svg>
<p class="abs" style="left:700px;top:2495px;font-family:var(--heading);font-size:11px;font-weight:600;text-transform:uppercase">Photo Shoots</p>
<p class="abs" style="left:700px;top:2511px;font-size:10px;line-height:15px">Stunning backdrops for<br>unforgettable pictures</p>
<div class="btn" style="left:645px;top:2574px;width:128px;height:38px">View Details</div>

<!-- testimonials -->
<p class="abs script" style="left:0;top:2723px;width:1200px;font-size:23px">Client Testimonials</p>
<h2 class="abs heading" style="left:0;top:2759px;width:1200px;font-size:30px">Our Happy Clients Say</h2>

<div class="abs review" style="left:27px;top:2853px;width:284px;height:167px">
  <div class="stars">★★★★★</div>
  <p class="quote">"The car was a dream come true. Every-one turned their heads! The chauffeur was polite and professional stress-free experience from start to finish!"</p>
  <div class="client"><span class="avatar"></span>-Ola &amp; Piotr</div>
</div>
<div class="abs review" style="left:325px;top:2825px;width:283px;height:166px">
  <div class="stars">★★★★★</div>
  <p class="quote">"The car was a dream come true. Every-one turned their heads! The chauffeur was polite and professional stress-free experience from start to finish!"</p>
  <div class="client"><span class="avatar"></span>-Ola &amp; Piotr</div>
</div>
<div class="abs review" style="left:623px;top:2825px;width:283px;height:166px">
  <div class="stars">★★★★★</div>
  <p class="quote">"The car was a dream come true. Every-one turned their heads! The chauffeur was polite and professional stress-free experience from start to finish!"</p>
  <div class="client"><span class="avatar"></span>-Ola &amp; Piotr</div>
</div>
<div class="abs review" style="left:920px;top:2853px;width:284px;height:167px">
  <div class="stars">★★★★★</div>
  <p class="quote">"The car was a dream come true. Every-one turned their heads! The chauffeur was polite and professional stress-free experience from start to finish!"</p>
  <div class="client"><span class="avatar"></span>-Ola &amp; Piotr</div>
</div>
<div class="abs dots"><span></span><span class="on"></span><span></span><span></span></div>

<!-- call to action -->
<section class="abs cta"></section>
<h2 class="abs heading" style="left:0;top:3143px;width:1200px;font-size:31px">Book Your Car Your Dream Car Awaits</h2>
<p class="abs" style="left:0;top:3188px;width:1200px;text-align:center;font-size:10.5px">Tell us about your wedding day and let us take care of the journey.</p>
<div class="btn" style="left:533px;top:3216px;width:130px;height:38px;background:#fff;box-shadow:0 0 0 3px var(--gold),0 0 0 4px #fff">Read More</div>

<!-- footer -->
<footer class="abs footer"></footer>
<div class="abs brand" style="left:193px;top:3369px;font-size:24px"><span class="brand-dot"></span>WeselneKarety</div>
<div class="btn" style="left:813px;top:3363px;width:207px;height:38px">Schedule a Consultation</div>
<nav class="abs footer-links"><span>HOME</span><span>ABOUT US</span><span>FLEET</span><span>SERVICES</span><span>WHY US</span><span>FAQ</span><span>CONTACT</span></nav>
<div class="abs hline" style="left:183px;top:3483px;width:833px"></div>
<div class="abs divider-v" style="left:434px;top:3483px;height:117px;background:#bbb"></div>
<div class="abs divider-v" style="left:766px;top:3483px;height:117px;background:#bbb"></div>
<div class="abs contact-col" style="left:183px;width:251px"><h3>Phone</h3><p>(123) 456- 7890</p></div>
<div class="abs contact-col" style="left:434px;width:332px"><h3>Address</h3><p>12 Lipowa Street<br>Kraków 30-001</p></div>
<div class="abs contact-col" style="left:766px;width:250px"><h3>Email</h3><p>info@weselnekarety.pl</p></div>
<div class="abs hline" style="left:183px;top:3600px;width:833px"></div>
<div class="abs socials"><span></span><span></span><span></span><span></span></div>
<p class="abs copy">2025 WeselnyKarety.pl - All Rights Reserved</p>

</body>
</html>
```